Business Card Design

We are looking for a business card designed for our landscaping company. We do landscaping installation & Maintenance Services. We would like to see designs that have basic landscaping in background. We also think it is important to have both of our names and phone numbers on the card. We need something that stands out a little whether it is shape of the card or thickness or design.

Industry/Entity Type

Business

Contact Information for Business Card

Pale Ridge Yardworks, paleridgeyardworks@mailbrook.net, Dale Purvine 555-213-7690, Martin Kolbey 555-864-1037

```html
<!DOCTYPE html>
<html lang="en">
<head>
<meta charset="utf-8">
<title>Pale Ridge Yardworks – Business Card</title>
<link rel="stylesheet" href="https://fonts.googleapis.com/css2?family=Arimo:wght@400;700&display=swap">
<style>
  :root {
    --card-bg: #ffffff;
    --brand-green: #43f800;
    --brand-green-soft: #6cfa3a;
    --on-green: #ffffff;
    --font-main: "Arimo", Arial, sans-serif;
  }
  html, body {
    margin: 0;
    padding: 0;
    overflow: hidden;
    background: var(--card-bg);
  }
  .business-card {
    position: relative;
    width: 1200px;
    height: 700px;
    background: var(--card-bg);
    font-family: var(--font-main);
    color: var(--brand-green);
    overflow: hidden;
  }
  .brand-panel {
    position: absolute;
    left: 88px;
    top: 111px;
    width: 415px;
    height: 381px;
  }
  .grass-art {
    position: absolute;
    inset: 0;
    background: linear-gradient(180deg, var(--brand-green) 0%, var(--brand-green) 35%, var(--brand-green-soft) 100%);
  }
  .brand-name {
    position: relative;
    margin: 0;
    padding-top: 18px;
    text-align: center;
    color: var(--on-green);
    font-size: 42px;
    font-weight: 400;
    line-height: 52px;
    letter-spacing: 0.3px;
    text-transform: uppercase;
  }
  .email {
    position: absolute;
    left: 568px;
    top: 326px;
    font-size: 35px;
    line-height: 40px;
    font-weight: 400;
    color: var(--brand-green);
    text-decoration: none;
  }
  .contacts {
    position: absolute;
    left: 88px;
    top: 514px;
    margin: 0;
    padding: 0;
    list-style: none;
    font-size: 31px;
    line-height: 42px;
  }
  .contact-name {
    font-weight: 700;
  }
</style>
</head>
<body>
  <main class="business-card">
    <header class="brand-panel">
      <div class="grass-art" role="img" aria-label="Green lawn with tall grass blades rising from the bottom edge"></div>
      <h1 class="brand-name">Pale Ridge<br>Yardworks</h1>
    </header>

    <a class="email" href="mailto:paleridgeyardworks@mailbrook.net">paleridgeyardworks@mailbrook.net</a>

    <ul class="contacts">
      <li><span class="contact-name">Dale Purvine</span> 555-213-7690</li>
      <li><span class="contact-name">Martin Kolbey</span> 555-864-1037</li>
    </ul>
  </main>
</body>
</html>
```